Redesign Login page

I want to redesign my login page to bring my 2 products closer together. I am only looking to redesign one login page, not 2.

For the logo, please make it solid and it can be black or white if helpful. I can also fine tune the logo if you get it close.

Coded - Design and coding required

1 page

```html
<!DOCTYPE html>
<html lang="en">
<head>
<meta charset="utf-8">
<title>Norvia – Log In</title>
<link rel="stylesheet" href="https://fonts.googleapis.com/css2?family=Noto+Sans:wght@400;500;700&display=swap">
<style>
  :root {
    --page-bg: #f7f7f7;
    --card-bg: #ffffff;
    --ink: #222422;
    --ink-soft: #444844;
    --muted: #8a8a8a;
    --border: #d6d6d6;
    --primary: #434840;
    --primary-text: #f4f4f2;
    --alt-bg: #f0f0f0;
    --brand: #3a3c3a;
  }
  * { box-sizing: border-box; margin: 0; padding: 0; }
  html, body {
    width: 1200px; height: 1200px; overflow: hidden;
    background: var(--page-bg);
    font-family: "Noto Sans", sans-serif;
    color: var(--ink);
  }
  .login-card {
    position: absolute; left: 345px; top: 172px;
    width: 494px; height: 883px;
    background: var(--card-bg);
    border-radius: 16px;
    box-shadow: 0 8px 30px rgba(0,0,0,0.06);
  }
  .login-card > * { position: absolute; left: 49px; width: 395px; }
  .brand {
    top: 30px; height: 84px;
    display: flex; align-items: center; justify-content: center; gap: 12px;
  }
  .brand-mark { width: 26px; height: 26px; background: var(--brand); border-radius: 4px; }
  .brand-name { font-size: 52px; font-weight: 700; color: var(--brand); letter-spacing: -1px; line-height: 1; }
  .title {
    top: 138px; text-align: center;
    font-size: 27px; font-weight: 700; line-height: 34px;
  }
  .field-label { font-size: 17px; color: var(--ink-soft); line-height: 22px; }
  .label-email { top: 194px; }
  .label-password { top: 307px; }
  .text-input {
    height: 62px; border: 1px solid var(--border); border-radius: 8px;
    padding: 0 16px; font: inherit; font-size: 18px; color: var(--ink);
    background: #fff;
  }
  .text-input::placeholder { color: #8a8a8a; }
  .input-email { top: 222px; }
  .input-password { top: 336px; height: 61px; }
  .options-row {
    top: 420px; height: 22px;
    display: flex; justify-content: space-between; align-items: center;
    font-size: 16px; color: var(--ink-soft);
  }
  .remember { display: flex; align-items: center; gap: 7px; }
  .remember input { width: 15px; height: 15px; margin: 0; }
  .forgot { color: var(--ink-soft); text-decoration: none; }
  .btn {
    height: 66px; border-radius: 8px; font: inherit; font-size: 19px;
    display: flex; align-items: center; justify-content: center;
  }
  .btn-primary { top: 472px; height: 65px; background: var(--primary); color: var(--primary-text); border: none; }
  .divider {
    top: 574px; height: 22px;
    display: flex; align-items: center; gap: 28px;
    color: var(--muted); font-size: 17px;
  }
  .divider::before, .divider::after { content: ""; flex: 1; height: 1px; background: #dcdcdc; }
  .btn-provider { top: 629px; height: 67px; background: #fff; border: 1px solid var(--border); color: var(--ink-soft); }
  .btn-provider-alt { top: 718px; height: 68px; background: var(--alt-bg); border: 1px solid var(--border); color: var(--ink-soft); }
  .signup {
    top: 808px; text-align: center; font-size: 17px; line-height: 24px; color: var(--ink);
  }
  .signup a { color: var(--ink-soft); text-decoration: none; }
</style>
</head>
<body>
  <main class="login-card">
    <div class="brand">
      <span class="brand-mark"></span>
      <span class="brand-name">Norvia</span>
    </div>
    <h1 class="title">Welcome Back</h1>
    <label class="field-label label-email" for="email">Email</label>
    <input class="text-input input-email" id="email" type="email" placeholder="Enter your email">
    <label class="field-label label-password" for="password">Password</label>
    <input class="text-input input-password" id="password" type="password" placeholder="Enter your password">
    <div class="options-row">
      <label class="remember"><input type="checkbox"> Remember Me</label>
      <a class="forgot" href="#">Forgot Password?</a>
    </div>
    <button class="btn btn-primary" type="submit">Log In</button>
    <div class="divider">OR</div>
    <button class="btn btn-provider" type="button">Continue with Glimmer</button>
    <button class="btn btn-provider-alt" type="button">Continue with Northgate</button>
    <p class="signup">Don’t have an account? <a href="#">Sign Up</a></p>
  </main>
</body>
</html>
```